Trucking company needs business card design

New trucking company needs fresh ideas on a business card. Contracted exclusively to ParcelWing, can incorporate their colors or style, but not necessary.
Calder Haulage, Inc (with or without the Inc.)
Dale Whitcombe, CEO
555-555-0147
PO BOX 372
Ridgeford, ID
Updates

Need to add my email address to the card--calderhaulageinc@roadmail.example

Industry/Entity Type

Trucking Company

```html
<!DOCTYPE html>
<html lang="en">
<head>
<meta charset="utf-8">
<title>Calder Haulage, Inc. — Business Card</title>
<link rel="stylesheet" href="https://fonts.googleapis.com/css2?family=Montserrat:wght@400;500;700&display=swap">
<style>
  :root {
    --page-bg: #e9e9e9;
    --card-bg: #1f1d1d;
    --brand-orange: #f07c22;
    --rule-grey: #6b6866;
    --text-white: #f4f4f4;
  }
  * { box-sizing: border-box; margin: 0; padding: 0; }
  html, body {
    width: 1066px;
    height: 1200px;
    overflow: hidden;
  }
  body {
    background: var(--page-bg);
    display: flex;
    align-items: center;
    justify-content: center;
    font-family: "Montserrat", sans-serif;
  }
  .business-card {
    width: 900px;
    height: 514px;
    background: var(--card-bg);
    border-radius: 30px;
    display: flex;
    flex-direction: column;
    justify-content: center;
    padding: 40px 70px;
  }
  .brand-block {
    align-self: center;
    display: flex;
    flex-direction: column;
    align-items: center;
  }
  .brand-name {
    color: var(--brand-orange);
    font-weight: 700;
    font-size: 58px;
    letter-spacing: 1px;
    line-height: 1;
    text-transform: uppercase;
    white-space: nowrap;
  }
  .brand-rule {
    width: 100%;
    height: 2px;
    background: var(--rule-grey);
    margin: 18px 0 14px;
  }
  .brand-email {
    color: var(--brand-orange);
    font-weight: 500;
    font-size: 27px;
    white-space: nowrap;
  }
  .dotted-divider {
    border: none;
    border-top: 4px dotted var(--brand-orange);
    margin: 40px 0 36px;
  }
  .contact-block {
    padding-left: 20px;
    color: var(--text-white);
  }
  .person-name {
    font-weight: 700;
    font-size: 50px;
    text-transform: uppercase;
    line-height: 1.1;
    white-space: nowrap;
  }
  .person-title {
    font-weight: 500;
    font-size: 38px;
  }
  .contact-line {
    margin-top: 14px;
    font-weight: 400;
    font-size: 30px;
    letter-spacing: 1px;
    text-transform: uppercase;
    white-space: nowrap;
  }
</style>
</head>
<body>
  <article class="business-card">
    <header class="brand-block">
      <p class="brand-name">Calder Haulage, Inc.</p>
      <div class="brand-rule"></div>
      <p class="brand-email">calderhaulageinc@roadmail.example</p>
    </header>
    <hr class="dotted-divider">
    <section class="contact-block">
      <p class="person-name">Dale Whitcombe,<span class="person-title">CEO</span></p>
      <p class="contact-line">PO Box 372 Ridgeford, ID | 555-555-0147</p>
    </section>
  </article>
</body>
</html>
```